Professional Commercial Cleaning Services

this website https://plomverservices.com.au/ already exists we just need someone to redesign and edit it. We had started this but not entirely sure how to design this ourselves.

We are a professional commercial cleaning business specialising in office, warehouse and restaurant cleaning. We would like to keep colours to black and white but are open to suggestions.

```html
<!DOCTYPE html>
<html lang="en">
<head>
<meta charset="utf-8">
<title>Why Choose Us – Plomver Services</title>
<link href="https://fonts.googleapis.com/css2?family=Montserrat:wght@400;500;600;700&display=swap" rel="stylesheet">
<style>
  :root {
    --navy: #15233f;
    --hero-navy: #222b45;
    --teal: #1fa59b;
    --teal-dark: #17958c;
    --orange: #f39a26;
    --text: #3c3c44;
    --white: #ffffff;
    --footer-line: #2d6a8a;
  }
  * { margin: 0; padding: 0; box-sizing: border-box; }
  html, body { width: 916px; height: 1200px; overflow: hidden; }
  body { font-family: "Montserrat", sans-serif; background: var(--white); position: relative; color: var(--text); }

  .hero { position: absolute; left: 0; top: 0; width: 916px; height: 286px;
    background: linear-gradient(90deg, #1c2540 0%, #242e4a 50%, #3a3f52 75%, #2c3249 100%); }
  .hero-photo { position: absolute; left: 480px; top: 0; width: 436px; height: 286px;
    background: radial-gradient(ellipse at 55% 60%, rgba(120,110,90,.45), rgba(34,43,69,0) 70%); }
  .brand { position: absolute; display: flex; align-items: center; gap: 6px;
    font-weight: 600; font-size: 14px; color: var(--teal); }
  .brand-dot { width: 12px; height: 12px; border-radius: 50%; background: var(--orange); }
  .hero .brand { left: 124px; top: 30px; }
  .nav { position: absolute; top: 31px; left: 0; width: 916px; font-size: 9px; font-weight: 600; color: var(--white); }
  .nav span { position: absolute; white-space: nowrap; }
  .nav .active { color: var(--orange); }
  .nav .phone { color: var(--orange); font-size: 12px; font-weight: 700; top: -2px; }
  .hero-title { position: absolute; left: 120px; top: 159px; font-size: 20px; font-weight: 700; color: var(--white); letter-spacing: .2px; }

  .gallery .pic { position: absolute; left: 120px; width: 172px; border-radius: 4px; }
  .pic-1 { top: 349px; height: 72px; background: linear-gradient(120deg, #c9b79a, #e8e2d6 50%, #a7886a); }
  .pic-2 { top: 434px; height: 72px; background: linear-gradient(120deg, #8a8f86, #d9d4cb 50%, #3f5f8c); }
  .pic-3 { top: 520px; height: 86px; background: linear-gradient(120deg, #5b6f88, #7d8ea4 50%, #2f8087); }
  .pic-4 { top: 619px; height: 72px; background: linear-gradient(120deg, #d7c4a3, #eae6df 50%, #6b7d5a); }

  .copy { position: absolute; left: 329px; top: 350px; width: 462px; font-size: 9.8px; line-height: 15.3px; }
  .copy p { margin-bottom: 15px; }

  .cta { position: absolute; left: 0; top: 755px; width: 916px; height: 251px;
    background: linear-gradient(90deg, #1fa59b 0%, #4f9d86 30%, #9aa55a 55%, #d69d33 75%, #e8a32c 100%); }
  .cta-title { position: absolute; left: 124px; top: 50px; font-size: 26px; line-height: 29px; font-weight: 700; color: var(--white); }
  .cta-text { position: absolute; left: 124px; top: 116px; width: 270px; font-size: 10px; line-height: 11.5px; color: var(--white); }
  .btn { position: absolute; top: 172px; height: 24px; border-radius: 12px; font-size: 8px; font-weight: 600;
    color: var(--white); display: flex; align-items: center; justify-content: center; }
  .btn-book { left: 124px; width: 78px; background: var(--teal-dark); }
  .btn-quote { left: 212px; width: 123px; background: var(--orange); }

  .footer { position: absolute; left: 0; top: 1006px; width: 916px; height: 194px; background: var(--navy); color: var(--white); }
  .footer .brand { left: 124px; top: 52px; }
  .contact { position: absolute; top: 73px; font-size: 8px; text-decoration: underline; color: #d7dbe6; display: flex; align-items: center; gap: 6px; }
  .contact-mail { left: 578px; }
  .contact-phone { left: 727px; }
  .divider { position: absolute; left: 124px; top: 106px; width: 668px; height: 1px; background: var(--footer-line); }
  .copyright { position: absolute; left: 126px; top: 125px; font-size: 7px; color: #d7dbe6; }
  .copyright b { color: var(--white); font-weight: 600; }
  .footer-links { position: absolute; top: 125px; left: 0; width: 916px; font-size: 7px; color: #d7dbe6; }
  .footer-links span { position: absolute; white-space: nowrap; }
</style>
</head>
<body>
  <header class="hero">
    <div class="hero-photo" role="img" aria-label="Two smiling cleaners in aprons and yellow gloves giving a thumbs up in a kitchen"></div>
    <div class="brand"><span class="brand-dot"></span>plomver services</div>
    <nav class="nav">
      <span style="left:350px">Home</span>
      <span style="left:403px">About Us</span>
      <span style="left:472px">Services</span>
      <span class="active" style="left:536px">Why choose us</span>
      <span style="left:631px">Contact Us</span>
      <span class="phone" style="left:718px">0491570110</span>
    </nav>
    <h1 class="hero-title">WHY CHOOSE US</h1>
  </header>

  <section class="gallery">
    <div class="pic pic-1" role="img" aria-label="Cleaner wiping a glass office table"></div>
    <div class="pic pic-2" role="img" aria-label="Cleaning team vacuuming and wiping an office lounge"></div>
    <div class="pic pic-3" role="img" aria-label="Two happy clients holding a yellow star"></div>
    <div class="pic pic-4" role="img" aria-label="Bright clean open-plan office with tables and plants"></div>
  </section>

  <section class="copy">
    <p>Choosing Plomver Services for your commercial cleaning needs means opting for a partner who truly cares about the cleanliness and well-being of your workspace. As a small, family-owned business based in Sydney, NSW, we bring a personal touch to our services. Since 2018, we have built a reputation for outstanding quality and attention to detail, ensuring that each space we clean meets the highest standards.</p>
    <p>Our team is dedicated to understanding your specific needs and tailoring our cleaning solutions accordingly, whether you run a bustling restaurant, a busy office, or a retail space. Our experienced staff approaches every job with professionalism and pride, treating your facility as if it were our own.</p>
    <p>Reliability is at the heart of what we do; we work around your schedule to minimise disruptions to your business operations, ensuring that your space remains pristine without interrupting your daily activities. Furthermore, our focus on customer satisfaction means we are always open to feedback and ready to make adjustments to meet your expectations. By choosing Plomver Services, you’re not just hiring a cleaning company—you’re investing in a partnership that values your business and its success.</p>
    <p>Let us take care of the cleaning, so you can focus on what you do best. Experience the difference that a dedicated, detail-oriented cleaning service can make in your commercial space. With Plomver Services, you can trust that your environment will be impeccably maintained, leaving a lasting impression on your clients and a healthy space for your employees.</p>
  </section>

  <section class="cta" role="img" aria-label="Cleaner in an orange apron standing at a kitchen bench, behind a teal to orange tint">
    <h2 class="cta-title">Talk to our<br>experts today!</h2>
    <p class="cta-text">Our experienced and professional cleaners are trained to communicate with our-clients in order to cater to individual requirements in your home</p>
    <span class="btn btn-book">Book Online</span>
    <span class="btn btn-quote">Contact Us For A Quote</span>
  </section>

  <footer class="footer">
    <div class="brand"><span class="brand-dot"></span>plomver services</div>
    <span class="contact contact-mail">
      <svg width="10" height="8" viewBox="0 0 10 8"><rect x="0" y="0" width="10" height="8" rx="1" fill="#3ab0e2"/><path d="M0.5 1 L5 4.5 L9.5 1" stroke="#15233f" stroke-width="1" fill="none"/></svg>
      info@plomverservices.com.au
    </span>
    <span class="contact contact-phone">
      <svg width="7" height="10" viewBox="0 0 7 10"><rect x="0.6" y="0.6" width="5.8" height="8.8" rx="1" stroke="#3ab0e2" stroke-width="1.2" fill="none"/></svg>
      0491570110
    </span>
    <div class="divider"></div>
    <p class="copyright">© 2024 All Rights Reserved <b>By Plomver services</b></p>
    <div class="footer-links">
      <span style="left:466px">Home</span>
      <span style="left:506px">About Us</span>
      <span style="left:558px">Services</span>
      <span style="left:606px">Terms &amp; Condition</span>
      <span style="left:688px">Privacy Policy</span>
      <span style="left:755px">Contact Us</span>
    </div>
  </footer>
</body>
</html>
```